Education Certificate

We need a modern yet professional Certificate for those who successfully pass / complete our online Training course.

There are various courses but ONE certificate design required.

the certificate needs to look extremely professional and of value.

```html
<!DOCTYPE html>
<html lang="en">
<head>
<meta charset="UTF-8">
<title>Certificate of Course Completion</title>
<link rel="stylesheet" href="https://fonts.googleapis.com/css2?family=Cinzel:wght@500;600&family=Pinyon+Script&family=Poppins:wght@400;500;600;700&display=swap">
<style>
  :root {
    --navy: #0b2a86;
    --navy-deep: #061d5e;
    --gold: #ffd000;
    --gold-dark: #b8860b;
    --ink: #1e1e1e;
    --grey: #6b6b6b;
    --paper: #ffffff;
    --backdrop: #e6e8e9;
  }
  * { margin: 0; padding: 0; box-sizing: border-box; }
  html, body {
    width: 800px; height: 1200px; overflow: hidden;
    background: var(--backdrop);
  }
  .canvas { position: relative; width: 800px; height: 1200px; }
  .certificate {
    position: absolute; left: 40px; top: 321px;
    width: 720px; height: 557px;
    background: var(--paper);
    box-shadow: 4px 6px 12px rgba(0,0,0,0.22);
    overflow: hidden;
    font-family: 'Poppins', sans-serif;
  }
  .artwork { position: absolute; inset: 0; width: 100%; height: 100%; }
  .brand {
    position: absolute; left: 53px; top: 56px;
    display: flex; align-items: flex-start; gap: 12px;
  }
  .brand-square { width: 14px; height: 14px; background: var(--navy); margin-top: 2px; }
  .brand-name {
    color: var(--navy); font-weight: 500; font-size: 13.5px;
    line-height: 16px; letter-spacing: 0.6px; text-transform: uppercase;
  }
  .title {
    position: absolute; left: 49px; top: 152px;
    font-family: 'Cinzel', serif; font-weight: 600;
    font-size: 47px; line-height: 1; color: var(--navy);
    letter-spacing: 0.5px;
  }
  .subtitle {
    position: absolute; left: 52px; top: 197px;
    font-family: 'Cinzel', serif; font-weight: 500;
    font-size: 16.5px; color: var(--grey); letter-spacing: 0.4px;
  }
  .presented-tag {
    position: absolute; left: 35px; top: 251px;
    width: 145px; height: 18px;
    background: linear-gradient(90deg, rgba(255,208,0,0) 0%, rgba(255,208,0,0.55) 35%, var(--gold) 70%);
  }
  .presented-label {
    position: absolute; left: 52px; top: 252px;
    font-weight: 700; font-size: 10.5px; letter-spacing: 3.6px;
    color: var(--navy); line-height: 16px;
  }
  .recipient {
    position: absolute; left: 50px; top: 270px;
    font-family: 'Pinyon Script', cursive; font-size: 60px;
    line-height: 1.1; color: var(--ink);
  }
  .statement {
    position: absolute; left: 52px; top: 355px;
    font-size: 11.3px; line-height: 14.5px; color: var(--ink);
  }
  .field {
    position: absolute; display: flex; align-items: baseline;
    font-size: 11px; color: var(--ink);
  }
  .field-line {
    flex: 1; margin-left: 6px;
    border-bottom: 1px dotted #555; height: 1px;
  }
  .field-course { left: 51px; top: 445px; width: 430px; }
  .field-date { left: 52px; top: 488px; width: 205px; }
  .field-signature { left: 270px; top: 488px; width: 211px; }
  .seal-year { font-family: 'Poppins', sans-serif; font-weight: 700; }
</style>
</head>
<body>
<div class="canvas">
  <section class="certificate">
    <svg class="artwork" viewBox="0 0 1267 981" preserveAspectRatio="none" aria-hidden="false">
      <defs>
        <linearGradient id="photoTone" x1="0" y1="0" x2="1" y2="1">
          <stop offset="0" stop-color="#0a2a8c"/>
          <stop offset="0.6" stop-color="#08206e"/>
          <stop offset="1" stop-color="#061a55"/>
        </linearGradient>
        <linearGradient id="sealGold" x1="0" y1="0" x2="1" y2="1">
          <stop offset="0" stop-color="#f3c84a"/>
          <stop offset="0.5" stop-color="#c8901a"/>
          <stop offset="1" stop-color="#8f5f08"/>
        </linearGradient>
      </defs>
      <path class="photo-area" role="img" aria-label="Photo of colleagues working together at a laptop, tinted navy blue"
            d="M772,0 L1267,0 L1267,796 L1188,838 Q1030,790 940,680 Q800,470 772,0 Z"
            fill="url(#photoTone)"/>
      <path class="accent-curve" d="M712,0 Q718,520 960,740 Q1050,820 1188,908 L1267,862"
            fill="none" stroke="var(--gold)" stroke-width="13"/>
      <g class="award-seal" transform="translate(1015,794)">
        <polygon points="0,-84 73,-42 73,42 0,84 -73,42 -73,-42" fill="#e9b52a"/>
        <polygon points="0,-76 66,-38 66,38 0,76 -66,38 -66,-38" fill="url(#sealGold)"/>
        <text x="0" y="8" text-anchor="middle" class="seal-year" font-size="36" fill="#fff">2024</text>
        <text x="0" y="38" text-anchor="middle" font-family="Poppins, sans-serif" font-weight="500" font-size="21" letter-spacing="3" fill="#fff">AWARD</text>
        <text x="0" y="-32" text-anchor="middle" font-size="16" fill="#fff3c0">★</text>
        <text x="0" y="64" text-anchor="middle" font-size="12" fill="#fff3c0">★ ★ ★</text>
      </g>
    </svg>

    <div class="brand">
      <span class="brand-square"></span>
      <div class="brand-name">Global<br>Service<br>Academy</div>
    </div>

    <h1 class="title">CERTIFICATE</h1>
    <p class="subtitle">OF COURSE COMPLETION</p>

    <div class="presented-tag"></div>
    <p class="presented-label">PRESENTED TO</p>
    <p class="recipient">Daniel Harper</p>

    <p class="statement">Your participaion is a testament to your<br>commitment to learning &amp; professional growth</p>

    <div class="field field-course"><span>Course</span><span class="field-line"></span></div>
    <div class="field field-date"><span>Date</span><span class="field-line"></span></div>
    <div class="field field-signature"><span>Signature</span><span class="field-line"></span></div>
  </section>
</div>
</body>
</html>
```